R. K. Dalby, CPA & Associates, LLC
Your Accounting, Finance, and Tax Specialist
R. K. Dalby, CPA & Associates, LLC -
Use specific fonts
open to fonts
Professional
Rennick K. Dalby, CPA
President
4718 Copper Wren Ave. West Palm Beach, FL 33952
rennickdalbycpa@mailnook.test

```html
<!DOCTYPE html>
<html lang="en">
<head>
<meta charset="utf-8">
<title>R. K. Dalby, CPA &amp; Associates, LLC — Stationery</title>
<link href="https://fonts.googleapis.com/css2?family=Cormorant+Garamond:wght@600&family=Open+Sans:wght@400;600&display=swap" rel="stylesheet">
<style>
  :root {
    --backdrop: #2b2b2d;
    --paper: #ffffff;
    --plum: #93326f;
    --plum-light: #c77aa9;
    --ink: #6d6d72;
    --ink-light: #9a9aa0;
  }
  * { box-sizing: border-box; margin: 0; padding: 0; }
  html, body { width: 1200px; height: 619px; overflow: hidden; }
  body { background: var(--backdrop); position: relative; font-family: "Open Sans", sans-serif; }

  .sheet { position: absolute; background: var(--paper); box-shadow: 0 4px 14px rgba(0,0,0,.45); overflow: hidden; }
  .band { position: absolute; left: 0; right: 0; top: 0; background: linear-gradient(180deg, var(--plum-light), var(--plum) 55%, var(--plum-light)); }

  .brand { position: absolute; display: flex; align-items: center; gap: 8px; }
  .brand-mark { width: 22px; height: 22px; border: 2px solid var(--plum); flex: none; }
  .brand-name { font-family: "Cormorant Garamond", serif; font-weight: 600; color: var(--plum); line-height: 1.05; letter-spacing: .04em; }
  .brand-name span { display: block; font-size: .62em; letter-spacing: .02em; }

  .footer-line { position: absolute; left: 0; right: 0; text-align: center; font-size: 6.5px; color: var(--ink); letter-spacing: .02em; }

  /* business card */
  .card { left: 19px; top: 379px; width: 209px; height: 197px; }
  .card .band { height: 58px; }
  .card-person { position: absolute; top: 10px; left: 12px; color: #fff; font-size: 6.5px; font-weight: 600; }
  .card .brand { left: 10px; top: 66px; }
  .card .brand-name { font-size: 19px; }
  .card-contact { position: absolute; left: 12px; top: 132px; font-size: 6px; color: var(--ink); line-height: 1.7; }

  /* letterhead */
  .letterhead { left: 257px; top: 24px; width: 444px; height: 571px; }
  .letterhead .band { height: 24px; }
  .letterhead .brand { left: 140px; top: 34px; }
  .letterhead .brand-name { font-size: 23px; }
  .letterhead .footer-line { bottom: 12px; }

  /* envelope back */
  .envelope-back { left: 720px; top: 36px; width: 456px; height: 264px; }
  .envelope-back svg { position: absolute; inset: 0; }
  .envelope-back .brand { left: 208px; top: 84px; }
  .envelope-back .brand-mark { width: 34px; height: 34px; }

  /* envelope front */
  .envelope-front { left: 720px; top: 312px; width: 456px; height: 271px; }
  .envelope-front .band { height: 26px; }
  .envelope-front .brand { left: 104px; top: 40px; }
  .envelope-front .brand-name { font-size: 22px; }
  .envelope-front .footer-line { bottom: 28px; }
</style>
</head>
<body>

  <div class="sheet card">
    <div class="band"></div>
    <p class="card-person">Rennick K. Dalby, CPA | President</p>
    <div class="brand">
      <div class="brand-mark"></div>
      <div class="brand-name">R. K. DALBY,<span>CPA &amp; Associates, LLC</span></div>
    </div>
    <div class="card-contact">
      <p>4718 Copper Wren Ave.</p>
      <p>West Palm Beach, FL 33952</p>
      <p>P: 561 555 0148 | F: 561 555 0149 | rennickdalbycpa@mailnook.test</p>
    </div>
  </div>

  <div class="sheet letterhead">
    <div class="band"></div>
    <div class="brand">
      <div class="brand-mark"></div>
      <div class="brand-name">R. K. DALBY,<span>CPA &amp; Associates, LLC</span></div>
    </div>
    <p class="footer-line">4718 Copper Wren Ave. West Palm Beach, FL 33952 | P: 561 555 0148 | F: 561 555 0149 | E: rennickdalbycpa@mailnook.test</p>
  </div>

  <div class="sheet envelope-back">
    <svg width="456" height="264" viewBox="0 0 456 264" aria-hidden="true">
      <polyline points="0,8 228,150 456,8" fill="none" stroke="#cfcfd4" stroke-width="1"/>
    </svg>
    <div class="brand"><div class="brand-mark"></div></div>
  </div>

  <div class="sheet envelope-front">
    <div class="band"></div>
    <div class="brand">
      <div class="brand-mark"></div>
      <div class="brand-name">R. K. DALBY,<span>CPA &amp; Associates, LLC</span></div>
    </div>
    <p class="footer-line">4718 Copper Wren Ave. West Palm Beach, FL 33952 | P: 561 555 0148 | F: 561 555 0149 | E: rennickdalbycpa@mailnook.test</p>
  </div>

</body>
</html>
```